Tamkor, a service provider dedicated to improving the performance of a website

Tamkor offers optimization and performance improvement for all types of websites (showcase sites, e-commerce, ...), with the aim of improving their ranking on Vintrel and their customer transformation rate. The main benefits consist in optimizing the factors of a site. In addition, we also offer content creation (description of product sheets, services, ...), Vintrel Ads campaign management, migration version for Prestashop / Wordpress, etc. The design must be a fresh image, dynamic, why not "fun", but also serious. No favorite color, carte blanche on this point;)

```html
<!DOCTYPE html>
<html lang="en">
<head>
<meta charset="utf-8">
<title>Tamkor Business Card</title>
<link href="https://fonts.googleapis.com/css2?family=Open+Sans:wght@400;600;700;800&display=swap" rel="stylesheet">
<style>
  :root {
    --backdrop: #2b2b2c;
    --card: #0d0d0e;
    --card-edge: #161617;
    --brand-blue: #3f59b3;
    --text-grey: #a7a7aa;
    --divider: #555558;
  }
  * { margin: 0; padding: 0; box-sizing: border-box; }
  html, body {
    width: 1200px; height: 900px; overflow: hidden;
    background: var(--backdrop);
    font-family: "Open Sans", Arial, sans-serif;
  }
  .card {
    position: absolute; left: 320px; width: 560px; height: 320px;
    background: linear-gradient(160deg, var(--card-edge), var(--card) 60%);
    overflow: hidden;
  }
  .card__stripe {
    position: absolute; left: 0; right: 0; bottom: 0; height: 9px;
    background: var(--brand-blue);
  }
  .card--front { top: 115px; }
  .brand-name {
    position: absolute; left: 0; right: 0; top: 108px;
    text-align: center; color: var(--brand-blue);
    font-weight: 800; font-size: 92px; letter-spacing: -2px; line-height: 1;
  }
  .card--back { top: 465px; }
  .person {
    position: absolute; right: 312px; top: 92px; text-align: left;
  }
  .person__name {
    color: var(--brand-blue); font-weight: 700; font-size: 19px;
    letter-spacing: 0.5px; line-height: 1.2;
  }
  .person__role { color: var(--text-grey); font-size: 15px; line-height: 1.3; }
  .divider {
    position: absolute; left: 270px; top: 86px; width: 1px; height: 96px;
    background: var(--divider);
  }
  .contacts {
    position: absolute; left: 290px; top: 86px; list-style: none;
  }
  .contacts li {
    display: flex; align-items: center; gap: 9px;
    color: var(--text-grey); font-size: 16px; line-height: 24px;
  }
  .contacts svg { width: 12px; height: 12px; fill: var(--brand-blue); flex: none; }
  .address {
    position: absolute; left: 100px; top: 226px;
    color: var(--text-grey); font-size: 16px;
  }
</style>
</head>
<body>
  <section class="card card--front">
    <div class="brand-name">Tamkor</div>
    <div class="card__stripe"></div>
  </section>

  <section class="card card--back">
    <div class="person">
      <div class="person__name">RALAN VOSK</div>
      <div class="person__role">Managing Director</div>
    </div>
    <div class="divider"></div>
    <ul class="contacts">
      <li><svg viewBox="0 0 12 12"><path d="M1 4c0-2 2-3 5-3s5 1 5 3v1H8V4H4v1H1z"/><rect x="2" y="6" width="8" height="5" rx="1"/></svg>044-555 218 904</li>
      <li><svg viewBox="0 0 12 12"><path d="M3 0h6a1 1 0 0 1 1 1v10a1 1 0 0 1-1 1H3a1 1 0 0 1-1-1V1a1 1 0 0 1 1-1zm0 2v8h6V2z"/></svg>044-555 218 904</li>
      <li><svg viewBox="0 0 12 12"><path d="M0 2h12v8H0zm1 1v.5l5 3 5-3V3z"/></svg>hello@tamkor.com</li>
      <li><svg viewBox="0 0 12 12"><circle cx="6" cy="6" r="6"/></svg>www.tamkor.com</li>
    </ul>
    <div class="address">48, Corvel Street Brenmark, 204817.</div>
    <div class="card__stripe"></div>
  </section>
</body>
</html>
```